HiItsJonBrell.com needs a modern, eye-catching business card design

My name is Jon Brell and I own a video training (software development industry) website. I need a business card design that is eye catching for when I travel to conferences or do seminars. I would prefer something simple but bold. Something along the lines of this: https://pixvaultstatic.example/gallery_img/530172/44018/44018_9917302_530172_image.jpg

Note that I do not have a specific logo, but I do have an caricature I use on my site of myself. I've not attached it because I'm not really a fan of having it on my business cards. I would prefer lettering instead of an image. You can go to my website (https://hiitsjonbrell.com) for inspiration.

I want to add the following information on my card (the order of these, their size, and their casing is up to you):

Jon Brell
jon@HiItsJonBrell.com
@HiItsJonBrell
HiItsJonBrell.com
vidsharehub.example/HiItsJonBrell

I would also like to have somewhere on the card a small ad that says "Get a free course at https://HiItsJonBrell.com/FreeCourse". Feel free to play with that wording or layout if you need. I would prefer this text to be at the bottom of the card and subtle. Some small eye-catching thing might be ok but nothing huge or garish.

I plan on printing this card at pressquill.example (https://www.pressquill.example/us/design-guidelines/business-cards.html). I would like it to be the standard size (3.66" x 2.16"). I would prefer rounded corners and horizontal orientation. This is a two-side design. I would prefer the side with all of the information be primarily white but I like color text (again, flexible on that). On the front side, I like simple. Maybe just HiItsJonBrell.com (casing on that is up to you - whatever looks and reads the best - that goes for all of the casing). As for font choices, I prefer a modern, clean font. For example, Open Sans Light can be a nice option.

Website Info (might be helpful for the card):
Color Palette

Darkest blue - #263246
Alternate blue - #2F4E6A
Light blue - #2A98C3
Orange - #FF6201
White - #FFFFFF

Font for Jon Brell Logo

Jellyka Estryas Handwriting
http://www.typecrate.example/jellyka_estryas_handwriting.font

Fonts for Site Content and VidShare Thumbnails

Lovelo (bold title font)
http://www.glyphmill.example/lovelo-font/

Open Sans (body font)
http://www.letterbarn.example/fonts/open-sans

Industry/Entity Type

Software Development

Contact Information for Business Card

Jon Brell
jon@HiItsJonBrell.com
@HiItsJonBrell
HiItsJonBrell.com
vidsharehub.example/HiItsJonBrell

Get a free course at https://HiItsJonBrell.com/FreeCourse

Colors

Designer to choose colors to be used in the design.

Requirements
Nice to have
• Modern color - maybe primarily a color on the front and then that color as an accent on the back.
Should not have
• Lots of colors - I LOVE color but do not want a rainbow of colors on the card.

```html
<!DOCTYPE html>
<html lang="en">
<head>
<meta charset="utf-8">
<title>Jon Brell Business Card</title>
<link href="https://fonts.googleapis.com/css2?family=Open+Sans:wght@300;400;700&display=swap" rel="stylesheet">
<style>
  :root {
    --canvas-bg: #cfebd5;
    --card-top: #284a6b;
    --card-mid: #22506f;
    --card-bottom: #2b5677;
    --text-light: #ffffff;
  }
  html, body {
    margin: 0;
    padding: 0;
    width: 1200px;
    height: 1000px;
    overflow: hidden;
    background: var(--canvas-bg);
    font-family: "Open Sans", Arial, sans-serif;
  }
  .canvas { position: relative; width: 1200px; height: 1000px; }
  .card { position: absolute; overflow: hidden; color: var(--text-light); }
  .card-surface {
    position: absolute;
    inset: 0;
    background: linear-gradient(180deg, var(--card-top) 0%, var(--card-mid) 50%, var(--card-bottom) 100%);
  }
  .card-front { left: 312px; top: 147px; width: 585px; height: 335px; }
  .card-back { left: 340px; top: 586px; width: 529px; height: 302px; }

  .front-wordmark {
    position: absolute; left: 0; right: 0; top: 137px;
    margin: 0;
    text-align: center; font-weight: 300; font-size: 60px; line-height: 1;
  }

  .contact-list {
    position: absolute; right: 9px; top: 46px;
    margin: 0; padding: 0; list-style: none; text-align: right;
  }
  .contact-list li { font-weight: 300; font-size: 28px; line-height: 37.7px; }
  .contact-list .contact-name { font-weight: 700; font-size: 27px; }

  .free-course {
    position: absolute; left: 0; width: 512px; top: 261px;
    margin: 0; text-align: center; font-weight: 400; font-size: 16px; line-height: 20px;
  }
</style>
</head>
<body>
<main class="canvas">

  <section class="card card-front">
    <div class="card-surface" role="img" aria-label="Blue background pattern of horizontal bands with soft diagonal overlays"></div>
    <h1 class="front-wordmark">hiitsJonBrell</h1>
  </section>

  <section class="card card-back">
    <div class="card-surface" role="img" aria-label="Blue background pattern of horizontal bands with soft diagonal overlays"></div>
    <ul class="contact-list">
      <li class="contact-name">Jon Brell</li>
      <li>jon@HiItsJonBrell.com</li>
      <li>@HiItsJonBrell</li>
      <li>HiItsJonBrell.com</li>
      <li>vidsharehub.example/HiItsJonBrell</li>
    </ul>
    <p class="free-course">Get a free course at<br>https://HiItsJonBrell.com/FreeCourse</p>
  </section>

</main>
</body>
</html>
```